Prom Night 2011 theme

I am looking for a theme to best represent a high school "prom night". Design will be printed on slightly smaller than business card size paper. This is a clean sheet design, nothing is out of bounds so use you imagination. Target audience is high school age students. Design should have text "Prom Night 2011" incorporated into it. Colors are limitless.

```html
<!DOCTYPE html>
<html lang="en">
<head>
<meta charset="utf-8">
<title>Prom Night 2011</title>
<link rel="stylesheet" href="https://fonts.googleapis.com/css2?family=Russo+One&display=swap">
<style>
  :root {
    --night: #000000;
    --silver-light: #f4f4f4;
    --silver-mid: #b9b9b9;
    --silver-dark: #8a8a8a;
    --gold-glow: #fbf6cf;
    --gold: #e9b81c;
    --gold-deep: #c8922a;
  }
  html, body {
    margin: 0;
    padding: 0;
    background: var(--night);
    overflow: hidden;
  }
  .prom-card {
    position: relative;
    width: 1200px;
    height: 777px;
    background: var(--night);
    overflow: hidden;
  }
  .headline {
    position: absolute;
    left: 0;
    top: 0;
    width: 1200px;
    height: 777px;
  }
  .headline text {
    font-family: "Russo One", "Arial Black", sans-serif;
    fill: url(#silver);
  }
  .dancer {
    position: absolute;
    left: 878px;
    top: 36px;
    width: 275px;
    height: 717px;
    border-radius: 120px 120px 40px 40px;
    background: radial-gradient(ellipse 60% 45% at 50% 48%, var(--gold-glow) 0%, var(--gold) 55%, var(--gold-deep) 100%);
  }
</style>
</head>
<body>
<main class="prom-card">
  <svg class="headline" viewBox="0 0 1200 777" aria-label="Prom Night 2011">
    <defs>
      <linearGradient id="silver" x1="0" y1="0" x2="1" y2="0" gradientUnits="objectBoundingBox" spreadMethod="repeat">
        <stop offset="0" stop-color="var(--silver-dark)"/>
        <stop offset="0.3" stop-color="var(--silver-light)"/>
        <stop offset="0.55" stop-color="var(--silver-mid)"/>
        <stop offset="0.8" stop-color="var(--silver-light)"/>
        <stop offset="1" stop-color="var(--silver-dark)"/>
      </linearGradient>
    </defs>
    <text class="title-prom" x="72" y="257" textLength="585" lengthAdjust="spacingAndGlyphs" rotate="-2 4 -3 2"><tspan font-size="220">P</tspan><tspan font-size="170">ROM</tspan></text>
    <text class="title-night" x="66" y="448" font-size="212" textLength="663" lengthAdjust="spacingAndGlyphs" rotate="3 -2 2 -3 4">NIGHT</text>
    <text class="title-year" x="84" y="669" font-size="228" textLength="561" lengthAdjust="spacingAndGlyphs" rotate="-3 2 4 -2">2011</text>
  </svg>
  <div class="dancer" role="img" aria-label="Golden glowing silhouette of a girl in a short party dress, hands on hips"></div>
</main>
</body>
</html>
```